Natural Foods Start-up Needs a Snack Food Packaging Design

We are a natural foods company doing it differently. We don’t care about the need for consumers to make better food choices according to their enlightened self-interest. Let’s face it, their own health or the planet’s health often doesn’t REALLY matter to them. So it doesn’t drive us. The bottom line is that they want food that tastes damn good. It’s OUR job to make sure it is healthy and sustainable, all while tasting better than industrial alternatives.
We are launching a line of a carnivorous/high protein food. Think nutritious value of fish but tastes nothing like fish. Think snack, fast food, something that truck drivers would like (heard the 9-minute VIGOR story? Learn in!). Food that you eat with your fingers, and you lick your fingers when you are done, maybe tasting some of the motor oil that is left on your fingers from the oil change you did yourself on your KVR.
We are “Tundra” because we want to be big but not grand. We are to the point, and use plain language. We use words like “Epic” and “Big” and “More” and “Sky”. Think Montana. Unfortunately, we are not very intuitive. But we don’t try too hard either, we don’t say we are “tough” or “hardy” or make any overwrought claims at all. We are a bit masculine, but the type of masculine energy that women don’t mind sometimes adopting themselves (of course we are not even a little sexist or asshole).
Package Design Guidelines
Package should be a clean, modern design that very simply tells you what is inside and why you should eat it. Should communicate good tasting food. Should also communicate “good for you” and “good for the planet” but these points should feel like afterthoughts.Remember, the customer buys this because it tastes good—later seeing that it is sustainable and healthy will only provide confirmation that they made the right choice (but NOT be the reason why they bought).
Name of product (for now) is “Tundra FoodOrganic Snack Food” (please use these words as a placeholder). This should be prominently displayed on the package, using a large typeface. “Tundra Food” can be larger than “Organic Snack Food”. Words like “Low in fat, high in protein, high in omega-3s, high in vitamins X, Y, Z and minerals A, B, C” should be displayed on the package front. Package should be the size/proportion of a small potato chip bag. Bag will be compostable plastic and will need a very large, prominent window to see product sealed inside.
Food comes in pieces and you can reach inside and pull one out and snack on it. It might compete with chips, beef jerky, nuts, or other such snacks. Should appeal to young buyers, probably mostly young professional men at first, but should also be accessible to women and children.
This Project is linked to Logo Design Project: http://work.craftpoolx.com/task.aspx?id=527390

```html
<!DOCTYPE html>
<html lang="en">
<head>
<meta charset="UTF-8">
<title>Tundra Foods – Beef Jerky Package</title>
<link href="https://fonts.googleapis.com/css2?family=Arvo:wght@400;700&family=Dancing+Script:wght@600&family=Arimo&display=swap" rel="stylesheet">
<style>
  :root {
    --paper-light: #efdcb6;
    --paper-mid: #dcc08f;
    --paper-dark: #b8965e;
    --ink: #231f1c;
    --brown: #3a2e24;
    --band: #231f20;
    --red: #c8202f;
    --white: #ffffff;
    --sage: #7a956a;
    --meat-dark: #4a1a18;
    --meat-mid: #8a3634;
    --icon: #4a3c30;
  }
  * { margin: 0; padding: 0; box-sizing: border-box; }
  html, body { width: 801px; height: 1200px; overflow: hidden; background: var(--paper-mid); }
  .package {
    position: relative;
    width: 801px;
    height: 1200px;
    overflow: hidden;
    background: radial-gradient(ellipse at 50% 50%, var(--paper-light) 0%, var(--paper-mid) 60%, var(--paper-dark) 100%);
  }
  .sunburst {
    position: absolute; inset: 0;
    background: repeating-conic-gradient(from 0deg at 50% 50%, rgba(255,255,255,0.10) 0deg 7deg, rgba(120,80,30,0.06) 7deg 14deg);
  }
  .brand {
    position: absolute; top: 200px; left: 0; width: 100%;
    text-align: center;
    font-family: 'Arvo', serif; font-weight: 400;
    font-size: 56px; line-height: 1;
    color: var(--ink);
  }
  .brand-tagline {
    position: absolute; top: 281px; left: 0; width: 100%;
    text-align: center;
    font-family: 'Arvo', serif; font-size: 12px; letter-spacing: 2px;
    color: var(--brown);
  }
  .title-band {
    position: absolute; top: 330px; left: 0; width: 100%; height: 101px;
    background: var(--band);
    border-top: 9px solid var(--red);
    border-bottom: 9px solid var(--red);
    display: flex; align-items: center; justify-content: center;
    font-family: 'Arvo', serif; font-weight: 700;
    font-size: 40px; letter-spacing: 3px;
    color: var(--white);
  }
  .product-name {
    position: absolute; top: 458px; left: 0; width: 100%;
    text-align: center;
    font-family: 'Arvo', serif; font-weight: 700;
    font-size: 86px; letter-spacing: 8px; line-height: 1;
    color: var(--brown);
  }
  .product-window {
    position: absolute; top: 578px; left: 125px; width: 551px; height: 255px;
    border-radius: 14px;
    background: radial-gradient(ellipse at 60% 40%, var(--meat-mid) 0%, var(--meat-dark) 100%);
    box-shadow: inset 0 0 12px rgba(0,0,0,0.5);
  }
  .taste-label {
    position: absolute; top: 815px; left: 193px; width: 447px; height: 71px;
    background: var(--sage);
    display: flex; align-items: center; justify-content: center;
    font-family: 'Dancing Script', cursive; font-weight: 600;
    font-size: 34px; color: var(--white);
    box-shadow: 0 6px 8px rgba(0,0,0,0.15);
  }
  .nutrition-claims {
    position: absolute; top: 928px; left: 0; width: 100%;
    text-align: center;
    font-family: 'Arimo', sans-serif; font-size: 16px;
    color: var(--ink);
  }
  .benefit-band {
    position: absolute; top: 978px; left: 0; width: 100%; height: 63px;
    background: var(--band);
    display: flex; align-items: center; justify-content: center;
    font-family: 'Arvo', serif; font-weight: 700;
    font-size: 29px; color: var(--white);
  }
  .benefit-band .emphasis {
    text-decoration: underline; text-decoration-color: var(--red);
    text-decoration-thickness: 3px; text-underline-offset: 5px;
  }
  .recycle-icon {
    position: absolute; top: 1062px; left: 368px; width: 64px; height: 60px;
  }
  .eco-note {
    position: absolute; top: 1137px; left: 0; width: 100%;
    text-align: center;
    font-family: 'Arimo', sans-serif; font-size: 18.5px;
    color: var(--ink);
  }
</style>
</head>
<body>
<main class="package">
  <div class="sunburst"></div>

  <h1 class="brand">Tundra Foods</h1>
  <p class="brand-tagline">GRASS FED JERKY</p>

  <div class="title-band">ORGANIC SNACK FOOD</div>

  <h2 class="product-name">BEEF JERKY</h2>

  <div class="product-window" role="img" aria-label="Window showing pieces of dark red beef jerky"></div>

  <div class="taste-label">Delicious Guilt Free Snack</div>

  <p class="nutrition-claims">Low in fat&nbsp; | &nbsp;High in protein&nbsp; | &nbsp;High in omega-3s&nbsp; | &nbsp;High in vitamins X, Y, Z and minerals A, B, C</p>

  <div class="benefit-band">All Natural • Healthy • Great for&nbsp;<span class="emphasis">YOU!</span></div>

  <svg class="recycle-icon" viewBox="0 0 64 60" aria-label="Recycle icon" role="img">
    <g fill="var(--icon)">
      <path d="M24 4 L36 4 L44 18 L50 14 L46 30 L31 27 L37 23 L31 12 L22 27 L12 21 Z"/>
      <path d="M52 26 L60 40 L54 50 L39 50 L39 57 L29 45 L39 34 L39 41 L51 41 L44 29 Z"/>
      <path d="M4 40 L12 26 L20 31 L22 24 L27 39 L13 45 L16 40 L10 50 L26 50 L26 58 L10 58 Q2 55 4 40 Z"/>
    </g>
  </svg>
  <p class="eco-note">Good for the environment</p>
</main>
</body>
</html>
```